larvoo.net

We are a IT Service for the valley. I want a clean website, with new Design, like animated pictures. We focus on IT. Give me your best design. What I'm looking for is eye catching. Works with Smart Phones, and iPad, Tab. Need a section for Submit a support tickets and Remote support. I'm looking for new ideals. I'm open mind, let me see what you guys can do.

Target Market(s)

My clients to see what service and products we have.

Industry/Entity Type

It Service

Requirements
Must have
• Able to submit a trouble tickets and works with Smart Phones, iPad, Tab.

```html
<!DOCTYPE html>
<html lang="en">
<head>
<meta charset="utf-8">
<title>Larvoo Technology – IT Service</title>
<link href="https://fonts.googleapis.com/css2?family=PT+Sans:wght@400;700&display=swap" rel="stylesheet">
<style>
:root{
  --bg:#d9d9d9;
  --panel:#f4f4f4;
  --ink:#3d3d3d;
  --muted:#4a4a4a;
  --client:#5e5e5e;
  --blue:#2c6092;
  --blue-dark:#24557f;
  --nav:#464646;
  --nav-side:#b3b3b3;
  --rule:#bdbdbd;
  --footer:#454545;
  --white:#ffffff;
}
*{box-sizing:border-box;margin:0;padding:0}
html,body{width:1200px;height:1200px;overflow:hidden}
body{background:radial-gradient(ellipse at 50% 20%,#ececec 0%,#dadada 45%,#d6d6d6 100%);font-family:"PT Sans",sans-serif;color:var(--ink)}
.stage{position:absolute;left:0;top:0;width:1280px;height:1280px;transform:scale(.9375);transform-origin:0 0}
.abs{position:absolute}
a{color:inherit;text-decoration:none}
.header{left:140px;top:40px;width:1000px;height:105px;background:var(--panel);border-radius:3px 3px 0 0}
.brand{left:32px;top:28px;color:var(--muted);font-weight:700;line-height:1}
.brand .name{font-size:36px;letter-spacing:1px;display:block}
.brand .sub{font-size:12px;letter-spacing:7.4px;display:block;margin-top:3px}
.utility{right:32px;font-size:13px;letter-spacing:.6px;color:var(--ink);display:flex;gap:10px;align-items:center}
.utility svg{width:12px;height:12px;fill:#444;margin-left:6px}
.nav{left:140px;top:145px;width:1000px;height:30px;background:var(--nav);display:flex;align-items:center;font-size:12.5px;font-weight:700;letter-spacing:1px;color:var(--white)}
.nav .home{width:100px;height:100%;background:var(--nav-side);display:flex;align-items:center;padding-left:32px}
.nav ul{list-style:none;display:flex}
.nav li{margin-left:32px}
.nav li:first-child{margin-left:33px}
.nav .search{position:absolute;right:0;top:0;width:197px;height:100%;background:var(--nav-side);display:flex;align-items:center;justify-content:center;color:#ececec}
.h-section{font-size:12.5px;font-weight:700;letter-spacing:1px;color:var(--ink);text-transform:uppercase;padding-bottom:8px;border-bottom:2px solid var(--rule)}
.photo{background:linear-gradient(135deg,#fafafa 0%,#d2d4d6 60%,#b9bcbe 100%);border:1px solid #c4c4c4}
.feature h3{font-size:12.5px;font-weight:700;letter-spacing:1px;color:var(--blue);margin-bottom:14px}
.feature p{font-size:12.5px;line-height:15px;letter-spacing:.5px}
.tabs{display:flex;justify-content:space-between;font-size:13px;letter-spacing:.6px}
.tabs span{display:flex;align-items:center;gap:8px}
.tabs svg{width:12px;height:12px;fill:#444}
.cta{left:830px;top:530px;width:310px;height:31px;background:var(--blue);color:var(--white);font-size:12.5px;font-weight:700;letter-spacing:1px;display:flex;align-items:center;justify-content:center;border-bottom:2px solid var(--blue-dark)}
.band{left:140px;top:600px;width:1000px;height:279px;background:var(--panel)}
.review h4{font-size:12.5px;font-weight:700;letter-spacing:1px}
.review .stars{color:var(--blue);font-size:12px;letter-spacing:9px;margin:4px 0 12px}
.review p{font-size:12.5px;line-height:15px;letter-spacing:.5px;padding-left:3px}
.tablet{background:linear-gradient(135deg,#4a3a3e 0%,#7b5f61 30%,#b9c2cc 55%,#2f3e5a 75%,#d8d8d8 100%)}
.fin h4{font-size:12.5px;font-weight:700;letter-spacing:.7px;margin-bottom:14px;white-space:nowrap}
.fin .item{position:relative;padding-left:23px;margin-bottom:21px}
.fin .item svg{position:absolute;left:0;top:2px;width:14px;height:12px;fill:#555}
.fin .item a{display:block;color:var(--blue);font-size:12.5px;letter-spacing:.6px;margin-bottom:3px}
.fin .item p{font-size:12.5px;line-height:15px;letter-spacing:.5px}
.clients{left:140px;top:980px;width:1000px;display:flex;justify-content:space-between;align-items:center;color:var(--client);font-weight:700;font-size:24px;letter-spacing:.3px}
.history h3{font-size:13px;font-weight:400;color:var(--blue);letter-spacing:.6px;margin-bottom:14px}
.history p{font-size:12.5px;line-height:15px;letter-spacing:.5px}
.footer{left:140px;top:1157px;width:1000px;height:81px;background:var(--footer);border-radius:0 0 3px 3px;color:var(--white);font-size:12.5px;font-weight:700;letter-spacing:.8px}
.footer .follow{right:32px;top:32px;display:flex;gap:16px;align-items:center}
.footer .follow .net{font-weight:400;color:#e2e2e2;letter-spacing:.5px}
</style>
</head>
<body>
<div class="stage">

  <header class="header abs">
    <div class="brand abs"><span class="name">LARVOO</span><span class="sub">TECHNOLOGY</span></div>
    <div class="utility abs" style="top:27px">
      <a href="#">Login<svg viewBox="0 0 12 12"><path d="M5 0h2v6H5z"/><path d="M3 2.2 4.1 3.4A3.5 3.5 0 1 0 7.9 3.4L9 2.2A5 5 0 1 1 3 2.2z"/></svg></a>
      <a href="#" style="margin-left:6px">Register<svg viewBox="0 0 12 12"><path d="M2 5h8v7H2z"/><path d="M3.5 5V3.5a2.5 2.5 0 0 1 5 0V5H7V3.5a1 1 0 0 0-2 0V5z"/></svg></a>
    </div>
    <div class="utility abs" style="top:60px">
      <a href="#">Support Tickets<svg viewBox="0 0 12 12"><path d="M6 0h6v6l-6 6-6-6z"/><circle cx="9.3" cy="2.7" r="1" fill="#f4f4f4"/></svg></a>
      <a href="#" style="margin-left:6px">Remote Support<svg viewBox="0 0 12 12"><path d="M6 0a4 4 0 0 1 4 4c0 3-4 8-4 8S2 7 2 4a4 4 0 0 1 4-4z"/><circle cx="6" cy="4" r="1.6" fill="#f4f4f4"/></svg></a>
    </div>
  </header>

  <nav class="nav abs">
    <a class="home" href="#">HOME</a>
    <ul>
      <li>ABOUT US</li><li>PRODUCTS</li><li>SUPPORT</li><li>LICENSING</li><li>DOWNLOAD</li><li>LATEST NEWS</li><li>CONTACT</li>
    </ul>
    <div class="search">SEARCH IN SITE</div>
  </nav>

  <h2 class="h-section abs" style="left:140px;top:212px;width:651px">All the reasons to secure your phone system</h2>
  <div class="photo abs" role="img" aria-label="White smartphone showing a grid of app icons" style="left:140px;top:276px;width:200px;height:285px"></div>

  <div class="feature abs" style="left:363px;top:273px;width:432px">
    <h3>CONTROL SYSTEMS</h3>
    <p>Telephone systems are just as vulnerable to phone hacker (phreaking) attacks as PCs and while most companies go to great lengths to protects their LANs and PCs from these attacks with ...</p>
  </div>
  <div class="feature abs" style="left:363px;top:380px;width:432px">
    <h3>DEFINITION TECHNOLOGY</h3>
    <p>The term "information technology" is used in a variety of senses. A wide definition is that of the Digital Systems Guild of America: "the study, design, development, application ...</p>
  </div>
  <div class="feature abs" style="left:363px;top:487px;width:432px">
    <h3>DATA STORAGE</h3>
    <p>Early electronic computers such as Codebreaker made use of punched tape, a long strip of paper on which data was represented by a series of holes a technology now obsolete ...</p>
  </div>

  <h2 class="h-section abs" style="left:830px;top:212px;width:310px">Commercial perspective</h2>
  <div class="tabs abs" style="left:830px;top:276px;width:310px">
    <span><svg viewBox="0 0 12 12"><circle cx="6" cy="3.2" r="3"/><path d="M0 12c0-4 3-5.5 6-5.5s6 1.5 6 5.5z"/></svg>Public Profile</span>
    <span><svg viewBox="0 0 12 12"><path d="M4 1h4v2H4z"/><path d="M0 3h12v8H0z"/><path d="M0 6h12v1H0z" fill="#d9d9d9"/></svg>Settings</span>
    <span><svg viewBox="0 0 12 12"><circle cx="6" cy="6" r="5.5" fill="none" stroke="#444" stroke-width="1.3"/><path d="M3 3c2 0 2 2 3 3s-1 3 0 4c-3 0-4-3-4-4s1-2 1-3zM8 2c0 2 2 2 2 4-2 0-2-2-2-4z"/></svg>Community</span>
  </div>
  <svg class="abs" style="left:830px;top:306px" width="310" height="202" viewBox="0 0 310 202" role="img" aria-label="Line chart of stored data rising over time">
    <path d="M0 0h310v187H170l-15 15-15-15H0z" fill="#bdbdbd"/>
    <rect x="9" y="9" width="292" height="168" fill="#f3f3f3"/>
    <g font-family="PT Sans,sans-serif" font-size="7" fill="#333">
      <text x="24" y="43">40</text><text x="24" y="71">30</text><text x="24" y="100">20</text><text x="24" y="128">10</text><text x="28" y="156">0</text>
    </g>
    <path d="M39 34v118h248" fill="none" stroke="#333" stroke-width=".8"/>
    <g stroke="#333" stroke-width=".8"><path d="M36 40h3M36 68h3M36 97h3M36 125h3"/></g>
    <polyline fill="none" stroke="#a9d4ee" stroke-width="1.2" points="62,125 73,122 84,117 95,119 107,110 118,116 130,104 141,112 153,100 164,106 176,98 187,114 199,106 210,94 221,110 232,88 244,96 255,70 266,78 277,60 286,44"/>
    <polyline fill="none" stroke="#4a9fd6" stroke-width="1.2" points="62,124 73,128 84,110 95,126 107,116 118,114 130,106 141,118 153,100 164,90 176,98 187,88 199,104 210,110 221,76 232,102 244,74 255,84 266,68 277,50 286,36"/>
    <polyline fill="none" stroke="#2b5b86" stroke-width="1.2" points="62,131 73,127 84,124 95,121 107,117 118,110 130,94 141,102 153,108 164,110 176,115 187,104 199,98 210,94 221,88 232,78 244,66 255,72 266,62 277,56 286,52"/>
  </svg>
  <div class="cta abs">MASSIVE AMOUNTS OF DATA ARE STORED</div>

  <section class="band abs">
    <div class="review abs" style="left:33px;top:28px;width:330px">
      <h4>TECHNOLOGY UPGRADE UI 1.23</h4>
      <div class="stars">★★★★★</div>
      <p>Telephone systems are just as vulnerable to phone attacks as PCs and while most companies go to great protects their LANs and PCs from these attacks ...</p>
    </div>
    <div class="review abs" style="left:33px;top:158px;width:330px">
      <h4>TECHNOLOGY UPGRADE UI 1.28</h4>
      <div class="stars">★★★★★</div>
      <p>Telephone systems are just as vulnerable to phone attacks as PCs and while most companies go to great protects their LANs and PCs from these attacks ...</p>
    </div>
    <div class="tablet abs" role="img" aria-label="Close-up of a tablet showing an agency website menu" style="left:387px;top:29px;width:293px;height:220px">
      <svg width="293" height="220" style="position:absolute;left:0;top:0"><path d="M146 0v220M0 109h293" stroke="#fff" stroke-width="1" opacity=".9"/></svg>
    </div>
    <div class="fin abs" style="left:718px;top:28px;width:270px">
      <h4>KNOWING YOUR FINANCIAL INFORMATION</h4>
      <div class="item"><svg viewBox="0 0 14 12"><path d="M2 12C2 6 5 4 9 4V1l5 4.5L9 10V7C6 7 4 8 2 12z"/></svg><a href="#">Make a payment</a><p>You can pay using your bank account, debit, or credit cards.</p></div>
      <div class="item"><svg viewBox="0 0 14 12"><path d="M2 12C2 6 5 4 9 4V1l5 4.5L9 10V7C6 7 4 8 2 12z"/></svg><a href="#">How to purchase online</a><p>The easiest way to remember your credit card number is not having to.</p></div>
      <div class="item"><svg viewBox="0 0 14 12"><path d="M2 12C2 6 5 4 9 4V1l5 4.5L9 10V7C6 7 4 8 2 12z"/></svg><a href="#">How to buy in stores</a><p>No matter where you shop, we don't charge you a transaction fee.</p></div>
    </div>
  </section>

  <h2 class="h-section abs" style="left:140px;top:916px;width:1000px">Our last clients and little history</h2>
  <div class="clients abs">
    <span class="client">labnote</span>
    <span class="client">kindshare</span>
    <span class="client">WALLSTAR</span>
    <span class="client">tapperks club</span>
    <span class="client">Northfield Build</span>
  </div>

  <div class="history abs" style="left:140px;top:1045px;width:1000px">
    <h3>Electronic computer Relay R3</h3>
    <p>Electronic computers, using either relays or valves, began to appear in the early 1940s. The electromechanical Relay R3, completed in 1941, was the world's first programmable computer, and by modern standards one of the first machines that could be considered a complete computing machine. Codebreaker, developed during the Second World War to decrypt German messages was the first electronic digital computer ...</p>
  </div>

  <footer class="footer abs">
    <div class="abs" style="left:31px;top:32px">Copyright © 2009-2012 Larvoo LLC</div>
    <div class="follow abs">Follow Larvoo On <span class="net">Pagebook</span><span class="net">Chirper</span><span class="net">Linkwork</span></div>
  </footer>

</div>
</body>
</html>
```